Calvanta Group Real Estate Company business cards

New business card design, we are generally happy with the basic layout of the existing front of business card, (feel free to change) but require a head shot photo on the back side.

http://www.calvanta.com.au/

Attached logos, and existing business card

------------------------------

Target Market(s)

Real estate

Industry/Entity Type

Real Estate

Contact Information for Business Card

Standard size double sided

Font styles to use
Other font styles liked:
• Futura

Requirements
Must have
• Photo head shot on the back side
Nice to have
• yes
Should not have
• No

```html
<!DOCTYPE html>
<html lang="en">
<head>
<meta charset="utf-8">
<title>Calvanta Group business cards</title>
<link href="https://fonts.googleapis.com/css2?family=Jost:wght@400;500&family=EB+Garamond:wght@400;500&display=swap" rel="stylesheet">
<style>
  :root {
    --bg: #2a2a2c;
    --card: #ffffff;
    --card-shade: #ececee;
    --purple: #2b1a5e;
    --purple-soft: #3a2a6e;
    --orange: #e88a1a;
    --grey: #9a9aa2;
    --white: #ffffff;
  }
  * { margin: 0; padding: 0; box-sizing: border-box; }
  html, body { width: 1200px; height: 873px; overflow: hidden; background: var(--bg); }
  .canvas { position: relative; width: 1200px; height: 873px; }
  .card {
    position: absolute; width: 560px; height: 320px; overflow: hidden;
    background: linear-gradient(160deg, var(--card) 0%, var(--card-shade) 100%);
    box-shadow: 0 10px 30px rgba(0,0,0,.55);
  }
  .card--front { left: 70px; top: 80px; }
  .card--back { left: 570px; top: 470px; }
  .skyline { position: absolute; left: 0; bottom: 0; width: 100%; height: 100%; }
  .brand { position: absolute; font-family: "Jost", sans-serif; color: var(--purple); line-height: 1; }
  .brand__name { font-weight: 400; letter-spacing: 1px; }
  .brand__sub { display: block; text-align: right; font-size: 9px; letter-spacing: 5px; color: var(--grey); margin-top: 2px; }
  .card--front .brand { left: 150px; top: 92px; }
  .card--front .brand__name { font-size: 52px; }
  .card--back .brand { left: 40px; top: 110px; }
  .card--back .brand__name { font-size: 60px; }
  .person { position: absolute; left: 46px; bottom: 28px; font-family: "EB Garamond", serif; }
  .person__name { color: var(--orange); font-size: 21px; letter-spacing: .5px; }
  .person__role { color: var(--white); font-size: 14px; }
  .contact { position: absolute; right: 30px; bottom: 50px; font-family: "EB Garamond", serif; color: var(--white); font-size: 14px; text-align: right; line-height: 1.9; }
  .contact__icon { display: inline-block; width: 8px; height: 8px; background: var(--orange); margin-left: 8px; vertical-align: middle; }
  .headshot { position: absolute; right: 0; top: 36px; width: 190px; height: 284px;
    background: linear-gradient(180deg, #d8d4d0 0%, #2c3448 55%, #222a3c 100%); }
  .web { position: absolute; left: 34px; bottom: 22px; font-family: "EB Garamond", serif; color: var(--white); font-size: 18px; letter-spacing: 4px; }
</style>
</head>
<body>
<div class="canvas">
  <section class="card card--front">
    <svg class="skyline" viewBox="0 0 560 320" preserveAspectRatio="none" role="img" aria-label="City skyline silhouette band">
      <polygon points="0,250 560,120 560,320 0,320" fill="var(--purple)"/>
    </svg>
    <div class="brand"><span class="brand__name">calvanta</span><span class="brand__sub">GROUP</span></div>
    <div class="person">
      <div class="person__name">Daniel Tran</div>
      <div class="person__role">Director</div>
    </div>
    <div class="contact">
      <div>0412 555 018<span class="contact__icon"></span></div>
      <div>daniel.tran@calvanta.com.au<span class="contact__icon"></span></div>
    </div>
  </section>

  <section class="card card--back">
    <svg class="skyline" viewBox="0 0 560 320" preserveAspectRatio="none" role="img" aria-label="City skyline silhouette band">
      <polygon points="0,250 560,190 560,320 0,320" fill="var(--purple)"/>
    </svg>
    <div class="brand"><span class="brand__name">calvanta</span><span class="brand__sub">GROUP</span></div>
    <div class="headshot" role="img" aria-label="Head shot photo of the director in a dark suit"></div>
    <div class="web">www.calvanta.com.au</div>
  </section>
</div>
</body>
</html>
```